Clearing a Court Debt Mark - Banner Ad for TR Website

I need a banner ad for a book I'm selling.

The book is about Clearing a Court Debt Mark, that is a County Court Judgment, from a credit report.

I have two websites. I want the banner ad to appear on
www.thornridgelaw.co.uk

It will then link to the new site: https://clearyourrecordguide.co.uk/

The first site already has a lot of traffic from visitors wanting to remove a CCJ. The purpose of that first site was originally for visitors to become clients of the law firm. However, most visitors can't afford legal advice and so I'd like to offer them the book instead.

I would like to see designs that use the colour green. The final design should communicate financial freedom, simplicity and trustworthiness.

Target Market(s)

Individuals who have discovered a CCJ on their credit report

Industry/Entity Type

Law

Font styles to use
Sans Serif

Colors
0054AA
0677BA
7BADD7
CADEEF
E8F1F8
0094D4
00A9DD
6FCCEA
C7EBF8
E9F6FB
00AB8E
00BBA5
67D7C9
C6EFE9
E9F9F6

Requirements
Must have
• Must fit at the end of a blog article, such as this one https://www.thornridgelaw.co.uk/ccj-wrong-address/

```html
<!DOCTYPE html>
<html lang="en">
<head>
<meta charset="utf-8">
<title>Clearing a Court Debt Mark – Banner</title>
<link rel="stylesheet" href="https://fonts.googleapis.com/css2?family=Barlow:wght@300;400;700;800&family=Montserrat:wght@500;700;800&family=Cinzel:wght@500&display=swap">
<style>
  :root{
    --page:#ffffff;
    --green-light:#5db43d;
    --green-mid:#45a02e;
    --green-dark:#2c7f22;
    --ink-green:#0b5a3b;
    --yellow:#eeff00;
    --white:#ffffff;
    --cover-red:#e8333a;
    --cover-ink:#1c1c1c;
    --cover-navy:#2a2238;
    --phone:#0d0d0d;
    --badge:#000000;
  }
  *{box-sizing:border-box;margin:0;padding:0}
  html,body{width:1200px;height:998px;overflow:hidden;background:var(--page)}
  body{position:relative;font-family:"Barlow",sans-serif}

  .banner{
    position:absolute;left:67px;top:115px;width:1066px;height:766px;
    background:radial-gradient(ellipse at 45% 50%,var(--green-light) 0%,var(--green-mid) 55%,var(--green-dark) 100%);
    overflow:hidden;
  }
  .abs{position:absolute}

  /* headline column */
  .help-icon{left:61px;top:77px;width:54px;height:58px;background:rgba(255,255,255,.85);border-radius:4px}
  .kicker{left:130px;top:74px;font-size:70px;font-weight:700;line-height:1;color:var(--white);letter-spacing:-.5px}
  .headline{left:46px;width:466px;text-align:center;color:var(--white);font-weight:800;line-height:1}
  .headline.removing{top:144px;font-size:97px;letter-spacing:-1px}
  .divider-a{left:100px;top:240px;width:372px;height:40px;display:flex;align-items:center;gap:14px;color:var(--white);font-weight:800;font-size:44px;line-height:1}
  .divider-a::before,.divider-a::after{content:"";flex:1;height:2px;background:var(--white)}
  .headline.ccj{top:270px;font-size:143px;color:var(--yellow);letter-spacing:2px}
  .title-pill{left:56px;top:415px;width:432px;height:43px;background:var(--white);border-radius:8px;
    display:flex;align-items:center;justify-content:center;color:var(--ink-green);
    font-weight:800;font-size:24px;letter-spacing:2.2px;text-transform:uppercase}
  .tagline{left:46px;top:465px;width:466px;text-align:center;color:var(--white);
    font-size:29px;font-weight:400;letter-spacing:1.5px;line-height:1.15}
  .chains-art{left:0;top:551px;width:530px;height:131px;
    background:linear-gradient(90deg,rgba(18,70,20,.45),rgba(18,70,20,.3) 50%,rgba(18,70,20,.45));border-radius:6px}

  /* book cover component */
  .cover{background:var(--white);display:flex;flex-direction:column;align-items:center;
    font-family:"Montserrat",sans-serif;color:var(--cover-ink);text-align:center}
  .cover-top{font-weight:800;font-size:26px;letter-spacing:1px;line-height:1}
  .cover-a{display:flex;align-items:center;gap:6px;width:130px;font-weight:800;font-size:16px;margin-top:8px}
  .cover-a::before,.cover-a::after{content:"";flex:1;height:2px;background:var(--cover-ink)}
  .cover-box{margin-top:8px;border:4px solid var(--cover-red);border-radius:6px;padding:6px 14px;
    color:var(--cover-red);font-weight:800;font-size:34px;line-height:1.05;letter-spacing:.5px}
  .cover-big{margin-top:6px;color:var(--cover-red);font-weight:800;font-size:88px;line-height:1;letter-spacing:-2px}
  .cover-sub{margin-top:12px;color:var(--cover-red);font-weight:700;font-size:11.5px;line-height:1.3;width:270px}
  .cover-sub .lead{color:var(--cover-ink);font-weight:500}
  .cover-art{margin-top:14px;width:205px;height:150px;border-radius:6px;
    background:linear-gradient(90deg,var(--cover-navy) 0 36%,#e9eef0 36% 100%)}
  .cover-author{margin-top:10px;font-family:"Cinzel",serif;font-size:30px;letter-spacing:3px;color:var(--cover-ink);line-height:1}
  .cover-role{margin-top:4px;font-family:"Cinzel",serif;font-size:15px;letter-spacing:3px;color:var(--cover-red)}

  .book{left:658px;top:65px;width:330px;height:607px;padding-top:26px;justify-content:flex-start;
    box-shadow:0 6px 18px rgba(0,0,0,.25)}
  .book .cover-art{margin-top:24px}

  .phone{left:530px;top:319px;width:186px;height:360px;background:var(--phone);border-radius:22px;
    box-shadow:0 6px 16px rgba(0,0,0,.35)}
  .phone-screen{position:absolute;left:9px;top:39px;width:169px;height:280px;overflow:hidden;background:var(--white)}
  .phone-screen .cover{width:330px;height:547px;padding-top:20px;transform:scale(.512);transform-origin:0 0}

  .store-badge{left:718px;top:684px;width:217px;height:61px;background:var(--badge);border:2px solid var(--white);
    border-radius:10px;display:flex;align-items:center;gap:12px;padding-left:22px;color:var(--white)}
  .store-badge .dot{width:22px;height:22px;border-radius:50%;background:var(--white);flex:none}
  .store-badge .label{display:flex;flex-direction:column;font-family:"Barlow",sans-serif;line-height:1.05}
  .store-badge .small{font-size:13px;font-weight:400}
  .store-badge .name{font-size:20px;font-weight:700}
</style>
</head>
<body>
  <a class="banner" href="https://clearyourrecordguide.co.uk/" aria-label="Clearing a Court Debt Mark – get the book">
    <div class="abs help-icon" role="img" aria-label="Pictogram of one person helping another up a step"></div>
    <div class="abs kicker">NEED HELP</div>
    <div class="abs headline removing">REMOVING</div>
    <div class="abs divider-a">A</div>
    <div class="abs headline ccj">CCJ?</div>
    <div class="abs title-pill">Clearing a Court Debt Mark</div>
    <p class="abs tagline">will help you to reach your<br>financial freedom.</p>
    <div class="abs chains-art" role="img" aria-label="Broken chain with birds flying free from the break"></div>

    <div class="abs cover book">
      <div class="cover-top">CLEARING</div>
      <div class="cover-a">A</div>
      <div class="cover-box">COURT DEBT</div>
      <div class="cover-big">MARK</div>
      <p class="cover-sub"><span class="lead">A SIMPLE JARGON-FREE GUIDE TO</span><br>REMOVING OF A COUNTY COURT JUDGMENT FROM YOUR CREDIT RECORD.</p>
      <div class="cover-art" role="img" aria-label="Illustration of a man cutting the chain to a debt ball and ball"></div>
      <div class="cover-author">HUGH FARRANT</div>
      <div class="cover-role">SOLICITOR</div>
    </div>

    <div class="abs phone">
      <div class="phone-screen">
        <div class="cover">
          <div class="cover-top">CLEARING</div>
          <div class="cover-a">A</div>
          <div class="cover-box">COURT DEBT</div>
          <div class="cover-big">MARK</div>
          <p class="cover-sub"><span class="lead">A SIMPLE JARGON-FREE GUIDE TO</span><br>REMOVING OF A COUNTY COURT JUDGMENT FROM YOUR CREDIT RECORD.</p>
          <div class="cover-art" role="img" aria-label="Illustration of a man cutting the chain to a debt ball and ball"></div>
          <div class="cover-author">HUGH FARRANT</div>
          <div class="cover-role">SOLICITOR</div>
        </div>
      </div>
    </div>

    <div class="abs store-badge">
      <span class="dot"></span>
      <span class="label"><span class="small">Available on</span><span class="name">Larkspur Books</span></span>
    </div>
  </a>
</body>
</html>
```